Business card

would like a double sided business card made up with my logos provided.
Prefer card to have black background and to use the black logos, with matching blue writing for the text.
One side to just be the logo, (Try to use both the black logos)
the other side to have the logo and also my credentials/business information.

Covering all aspects of Carpentry and Building Services

Marcus Tolvey
Qualified Carpenter
Mob: 0417263948
Email: rkt.joinery@mailbright.com
ABN: 47 615 209 834

Industry/Entity Type

Business

Contact Information for Business Card

Marcus Tolvey
Qualified Carpenter
Mob: 0417263948
ABN: 47 615 209 834

Requirements
Must have
• Please try to use both the black logos and incorporate into the card.

```html
<!DOCTYPE html>
<html lang="en">
<head>
<meta charset="utf-8">
<title>RKT Carpentry – Business Card</title>
<link href="https://fonts.googleapis.com/css2?family=Open+Sans:wght@400;600;700&display=swap" rel="stylesheet">
<style>
  :root{
    --page:#ececec;
    --card-white:#ffffff;
    --card-grey:#e3e4e6;
    --card-black:#080808;
    --ink:#1e1e1e;
    --blue:#1c7ed6;
    --navy:#0f1f5c;
    --navy-light:#1d4fa3;
    --strip:#4a4a4a;
    --white:#ffffff;
  }
  *{box-sizing:border-box;margin:0;padding:0}
  html,body{width:1200px;height:1102px;overflow:hidden;background:var(--page);font-family:"Open Sans",Arial,sans-serif}
  .canvas{position:relative;width:1200px;height:1102px}
  .card{position:absolute;left:150px;width:900px;height:500px;overflow:hidden;box-shadow:0 6px 18px rgba(0,0,0,.18)}
  .card--details{top:34px;background:linear-gradient(180deg,var(--card-white) 0%,var(--card-grey) 100%)}
  .card--brand{top:568px;background:var(--card-black)}
  .bands{position:absolute;inset:0;width:900px;height:500px}
  .wordmark{position:absolute;display:flex;align-items:center;gap:14px}
  .wordmark__mark{width:26px;height:26px;background:var(--blue)}
  .wordmark__name{font-weight:700;letter-spacing:1px;color:var(--ink)}
  .details-logo{left:150px;top:150px}
  .details-logo .wordmark__name{font-size:46px}
  .tagline{position:absolute;color:var(--blue);font-size:13px;letter-spacing:1.5px;font-weight:600}
  .details-tagline{left:190px;top:212px}
  .divider{position:absolute;left:470px;top:250px;width:2px;height:64px;background:#555}
  .person{position:absolute;left:160px;top:258px;text-align:center}
  .person__name{color:var(--blue);font-weight:700;font-size:24px}
  .person__title{color:var(--ink);font-size:22px}
  .contact{position:absolute;left:500px;top:240px;font-size:17px;color:var(--ink);line-height:1.35}
  .contact__row{display:flex;align-items:center;gap:8px}
  .contact__row svg{width:16px;height:16px;flex:none}
  .contact__indent{padding-left:24px;font-weight:600}
  .email{position:absolute;left:40px;top:430px;color:var(--white);font-size:20px;display:flex;align-items:center;gap:10px}
  .email svg{width:20px;height:20px}
  .brand-logo{position:absolute;left:0;right:0;top:150px;text-align:center}
  .brand-logo__name{display:inline-flex;align-items:center;gap:22px;font-weight:700;color:var(--white);font-size:110px;letter-spacing:4px;line-height:1}
  .brand-logo__mark{width:56px;height:56px;background:var(--blue)}
  .brand-logo__sub{color:var(--white);font-size:40px;letter-spacing:4px;margin-top:10px}
  .brand-logo__tag{color:var(--blue);font-size:22px;letter-spacing:2px;margin-top:4px}
</style>
</head>
<body>
<div class="canvas">
  <section class="card card--details">
    <svg class="bands" viewBox="0 0 900 500" aria-hidden="true">
      <defs>
        <linearGradient id="navyBand" x1="0" y1="0" x2="1" y2="0">
          <stop offset="0" stop-color="#0f1f5c"/>
          <stop offset=".6" stop-color="#1d4fa3"/>
          <stop offset="1" stop-color="#0f1f5c"/>
        </linearGradient>
      </defs>
      <polygon points="580,412 602,374 900,352 900,412" fill="url(#navyBand)"/>
      <polygon points="592,412 611,380 900,359 900,364 615,385 598,412" fill="#ffffff" opacity=".45"/>
      <polygon points="0,412 580,412 555,470 0,470" fill="#4a4a4a"/>
    </svg>
    <div class="wordmark details-logo">
      <span class="wordmark__mark"></span>
      <span class="wordmark__name">RKT CARPENTRY</span>
    </div>
    <div class="tagline details-tagline">CARPENTERS AND BUILDERS</div>
    <div class="person">
      <div class="person__name">Marcus Tolvey</div>
      <div class="person__title">Qualified Carpenter</div>
    </div>
    <div class="divider"></div>
    <div class="contact">
      <div class="contact__row">
        <svg viewBox="0 0 16 16"><rect x="4" y="1" width="8" height="14" rx="1.5" fill="#1e1e1e"/><rect x="5.5" y="3" width="5" height="8" fill="#fff"/></svg>
        <span>: 0417263948</span>
      </div>
      <div class="contact__row">
        <svg viewBox="0 0 16 16"><circle cx="8" cy="8" r="7" fill="none" stroke="#1e1e1e" stroke-width="1.6"/><text x="8" y="11.5" font-size="9" text-anchor="middle" fill="#1e1e1e" font-family="Arial">#</text></svg>
        <span>: 47 615 209 834</span>
      </div>
      <div class="contact__indent">Street Name, City Name</div>
      <div class="contact__indent">Zip Code-00000</div>
    </div>
    <div class="email">
      <svg viewBox="0 0 20 20"><rect x="2" y="5" width="16" height="11" rx="1" fill="#fff"/><polyline points="2,5 10,11 18,5" fill="none" stroke="#4a4a4a" stroke-width="1.5"/></svg>
      <span>: rkt.joinery@mailbright.com</span>
    </div>
  </section>

  <section class="card card--brand">
    <div class="brand-logo">
      <div class="brand-logo__name"><span class="brand-logo__mark"></span>RKT</div>
      <div class="brand-logo__sub">CARPENTRY</div>
      <div class="brand-logo__tag">CARPENTERS AND BUILDERS</div>
    </div>
  </section>
</div>
</body>
</html>
```